Tarvel Ridge LLC

Need Professional Business cards for New Investment Fund

Target Market(s)

High Quality investors

Industry/Entity Type

Financial

Contact Information for Business Card

Phone Number +1 555 284 6193
Name Pavel Orlinsky
Title Fund Manager
email po@FundTarvel.example
Website www.FundTarvel.example

Colors

Designer to choose colors to be used in the design.

Requirements
Must have
• Must have our Logo and all of the above. Must be made so lettering and loge can be raised

```html
<!DOCTYPE html>
<html lang="en">
<head>
<meta charset="utf-8">
<title>Tarvel Ridge LLC — Business Cards</title>
<link href="https://fonts.googleapis.com/css2?family=Quicksand:wght@500&display=swap" rel="stylesheet">
<style>
  :root {
    --backdrop: #d8805f;
    --card-green: #04462a;
    --panel-green: #26543e;
    --band-green: #2d5a45;
    --text-light: #e4e8e4;
    --accent-green: #4cb848;
    --card-shadow: rgba(80, 30, 10, 0.35);
  }
  * { margin: 0; padding: 0; box-sizing: border-box; }
  html, body { width: 1200px; height: 655px; overflow: hidden; }
  body {
    background: var(--backdrop);
    font-family: "Quicksand", sans-serif;
    font-weight: 500;
    color: var(--text-light);
    position: relative;
  }
  .card {
    position: absolute;
    top: 153px;
    width: 540px;
    height: 349px;
    background: var(--card-green);
    box-shadow: 4px 6px 10px var(--card-shadow);
  }
  .card--front { left: 40px; }
  .card--back { left: 620px; }

  .front__name {
    position: absolute;
    left: 0; right: 0;
    top: 132px;
    text-align: center;
    font-size: 34px;
    letter-spacing: 0.3px;
  }
  .front__band {
    position: absolute;
    left: 0; right: 0;
    top: 185px;
    height: 28px;
    background: var(--band-green);
    text-align: center;
    font-size: 17px;
    line-height: 28px;
  }

  .back__panel {
    position: absolute;
    inset: 25px 26px 25px 26px;
    background: var(--panel-green);
  }
  .brand {
    position: absolute;
    left: 12px;
    top: 22px;
    display: flex;
    align-items: center;
    gap: 8px;
    font-size: 16px;
    color: var(--text-light);
  }
  .brand__mark {
    width: 12px;
    height: 12px;
    background: var(--accent-green);
  }
  .contact {
    position: absolute;
    left: 12px;
    top: 202px;
    list-style: none;
    font-size: 18px;
    line-height: 31px;
  }
</style>
</head>
<body>
  <section class="card card--front" aria-label="Card front">
    <h1 class="front__name">Pavel Orlinsky</h1>
    <p class="front__band">Title Fund Manager</p>
  </section>

  <section class="card card--back" aria-label="Card back">
    <div class="back__panel">
      <div class="brand">
        <span class="brand__mark"></span>
        <span class="brand__name">Tarvel Ridge</span>
      </div>
      <ul class="contact">
        <li>+1 555 284 6193</li>
        <li>po@FundTarvel.example</li>
        <li>www.FundTarvel.example</li>
      </ul>
    </div>
  </section>
</body>
</html>
```